Design a For Sale sign board and Direction Sign Board.
Attached is an example of what i am thinking but am happy to look at any options.
Colours are to be ""bright Orange"on white and in reverse as well.

Logo Text

Logo id Brookvale & Co Real Estate.

```html
<!DOCTYPE html>
<html lang="en">
<head>
<meta charset="utf-8">
<title>Brookvale &amp; Co Real Estate – Agent Sign</title>
<link rel="stylesheet" href="https://fonts.googleapis.com/css2?family=Open+Sans:wght@700&display=swap">
<style>
  :root {
    --brand-orange: #ef512f;
    --sign-white: #ffffff;
  }
  html, body {
    margin: 0;
    padding: 0;
    overflow: hidden;
    background: var(--sign-white);
  }
  .sign {
    position: relative;
    width: 1200px;
    height: 927px;
    background: var(--sign-white);
    font-family: "Open Sans", sans-serif;
    font-weight: 700;
    overflow: hidden;
  }
  .brand-band {
    position: absolute;
    left: 0;
    top: 0;
    width: 1200px;
    height: 457px;
    background: var(--brand-orange);
    display: flex;
    align-items: center;
    justify-content: center;
    gap: 28px;
  }
  .brand-square {
    width: 48px;
    height: 48px;
    background: var(--sign-white);
    flex: none;
  }
  .brand-name {
    margin: 0;
    font-size: 56px;
    line-height: 1;
    color: var(--sign-white);
    white-space: nowrap;
  }
  .agent-name,
  .agent-phone {
    position: absolute;
    left: 0;
    width: 1200px;
    margin: 0;
    line-height: 1;
    white-space: nowrap;
    text-align: center;
    color: var(--brand-orange);
  }
  .agent-name {
    top: 521px;
    font-size: 185px;
    letter-spacing: -3px;
  }
  .agent-phone {
    top: 711px;
    font-size: 160px;
    letter-spacing: 0;
  }
</style>
</head>
<body>
  <main class="sign">
    <header class="brand-band">
      <span class="brand-square" aria-hidden="true"></span>
      <p class="brand-name">Brookvale &amp; Co Real Estate</p>
    </header>
    <section class="agent-contact">
      <p class="agent-name">Daniel Hart</p>
      <p class="agent-phone">0412 738 260</p>
    </section>
  </main>
</body>
</html>
```